Thornwell Building Company - advertisement poster

I am looking to print some canvas signs to advertise my general contracting company, Thornwell Building Company. The sign will measure 6' long x 3' high so the size should match that ratio. I already have a logo icon, which is the Letter 'A' and some trees that I would like to incorporate, see attached. I would also like the to have the following information listed:
1) phone number: 472-318-6095
2) email: thornwellbuildingcompany@mailvistra.net
3) website: thornwellbuildingcompany.com
4) Lic#5386204
5) I want to use this text: "BUILD WITH THE T-CREW!"

The ad should be relatively simple and clean. Black and Green are my company colors. I am open to creative ideas!

Target Market(s)

People looking to renovate their homes

Industry/Entity Type

Construction

Colors
59FF00
82FF00
B8FF75
E3FFCB
F4FFEA

Requirements
Must have
• Must have my company logo
Should not have
• No photos or complex graphics

```html
<!DOCTYPE html>
<html lang="en">
<head>
<meta charset="utf-8">
<title>Thornwell Building Company – Banner</title>
<link href="https://fonts.googleapis.com/css2?family=Montserrat:wght@400;600;700&family=Yellowtail&display=swap" rel="stylesheet">
<style>
  :root {
    --page: #252b2c;
    --ink: #060708;
    --green: #62e802;
    --white: #ffffff;
  }
  * { margin: 0; padding: 0; box-sizing: border-box; }
  html, body { width: 1200px; height: 676px; overflow: hidden; background: var(--page); }
  .banner {
    position: absolute; left: 0; top: 38px; width: 1200px; height: 600px;
    background: var(--ink); overflow: hidden;
    font-family: "Montserrat", Arial, sans-serif; color: var(--white);
  }
  .side-shape { position: absolute; top: 0; width: 300px; height: 600px; }
  .side-shape--left { left: 0; }
  .side-shape--right { right: 0; }
  .center { position: absolute; left: 0; right: 0; text-align: center; }
  .brand-mark {
    position: absolute; top: 44px; left: 550px; width: 100px; height: 100px;
    border-radius: 50%; background: var(--green);
  }
  .brand-name { top: 156px; font-weight: 700; line-height: 1; color: var(--white); }
  .brand-name__main { display: block; font-size: 48px; letter-spacing: 2px; }
  .brand-name__sub { display: block; font-size: 18px; letter-spacing: 9.5px; margin-top: 10px; padding-left: 9px; }
  .license {
    top: 232px; left: 539px; right: auto; width: 122px; height: 22px;
    border-radius: 11px; background: var(--green);
    font-size: 13px; line-height: 22px; font-weight: 400;
  }
  .tagline {
    top: 280px; font-family: "Yellowtail", cursive; font-size: 58px; line-height: 1.1; word-spacing: 2px;
  }
  .contact-label { top: 424px; font-size: 16px; font-weight: 700; letter-spacing: 0.3px; }
  .phone { top: 443px; font-size: 50px; font-weight: 700; color: var(--green); letter-spacing: -0.5px; line-height: 1.1; }
  .phone-rule { position: absolute; top: 501px; left: 486px; width: 229px; height: 2px; background: var(--green); }
  .contact-line {
    top: 510px; display: flex; justify-content: center; align-items: center; gap: 7px;
    font-size: 17px; font-weight: 400; line-height: 22px;
  }
  .contact-line--web { top: 539px; }
  .contact-line svg { width: 19px; height: 19px; flex: none; }
</style>
</head>
<body>
  <main class="banner">
    <svg class="side-shape side-shape--left" viewBox="0 0 300 600" role="img" aria-label="Green stepped pine tree shape">
      <polygon points="0,0 176,225 93,225 225,393 136,393 298,600 0,600" fill="var(--green)"/>
    </svg>
    <svg class="side-shape side-shape--right" viewBox="0 0 300 600" role="img" aria-label="Green stepped pine tree shape">
      <polygon points="300,0 124,225 207,225 75,393 164,393 2,600 300,600" fill="var(--green)"/>
    </svg>

    <div class="brand-mark" role="img" aria-label="Company logo mark"></div>

    <h1 class="center brand-name">
      <span class="brand-name__main">THORNWELL</span>
      <span class="brand-name__sub">BUILDING COMPANY</span>
    </h1>

    <div class="center license">LIC#5386204</div>

    <p class="center tagline">Build With The T-Crew!</p>

    <p class="center contact-label">CONTACT US NOW!</p>
    <p class="center phone">472-318-6095</p>
    <div class="phone-rule"></div>

    <p class="center contact-line">
      <svg viewBox="0 0 20 20" aria-hidden="true"><rect x="1.5" y="4" width="17" height="12" rx="1.5" fill="none" stroke="var(--green)" stroke-width="1.6"/><polyline points="2,5 10,11.5 18,5" fill="none" stroke="var(--green)" stroke-width="1.6"/></svg>
      thornwellbuildingcompany@mailvistra.net
    </p>
    <p class="center contact-line contact-line--web">
      <svg viewBox="0 0 20 20" aria-hidden="true"><circle cx="10" cy="10" r="8.3" fill="none" stroke="var(--green)" stroke-width="1.5"/><ellipse cx="10" cy="10" rx="3.6" ry="8.3" fill="none" stroke="var(--green)" stroke-width="1.3"/><line x1="1.7" y1="10" x2="18.3" y2="10" stroke="var(--green)" stroke-width="1.3"/></svg>
      thornwellbuildingcompany.com
    </p>
  </main>
</body>
</html>
```